Lantern Square, Steady Course. (Website Design)

We are launching a new bipartisan civic movement: Lantern Square. Steady Course.
The mission is this: Americans deserve a government that is legally required to serve them honestly.
We are looking for a world-class website designer capable of creating an emotionally powerful, modern, cinematic landing page experience that feels larger than politics.
This is not a campaign website for a political party or candidate. We are not looking for a red, white, and blue page with stripes, or American flags, or stock footage of smiling people in a voting booth. We are looking for an emotional and cinematic experience through and through.
The visual direction should feel:
Historic
Hopeful
American
Emotional
Cinematic
Trustworthy
Timeless
The goal is to make visitors feel that they are witnessing the beginning of something important and want to be part of it in the end.
Primary Objective:
Inspire visitors to participate in a one-minute survey and cast their vote.
The survey itself is extremely short and takes approximately one minute to complete.
Everything on the page should ultimately guide visitors toward this action while creating enough curiosity, trust, emotional engagement, and excitement that they feel compelled to take part in the movement.
Audience:
The audience is ordinary Americans across the political spectrum: Democrats, Republicans, Independents.
The design should feel unifying and welcoming.
It should avoid looking partisan, ideological, activist, or government-issued.
Creative Freedom:
We are intentionally giving designers substantial creative freedom.
We are not looking for someone to simply arrange content into predefined sections.
Instead, we are looking for a designer who can think strategically about user experience and persuasion.
The ideal design is as minimal as possible, but you may always:
Use as many sections as you believe are necessary.
Use as many images as you believe are necessary.
Include storytelling elements.
Include data visualizations.
Include timelines.
Include videos.
Include animations.
Include or exclude sections as you see fit.
Reorganize the flow entirely.
We uploaded some files containing text and section suggestions. You don’t have to use them.
We also uploaded some images to convey the general feel we’re looking for.
We are much more interested in the effectiveness of the overall experience than in any specific layout.
What success looks like:
Think outside the box.
Please do not create another generic political website. We have already explored those approaches.
We are looking for something different.
The winning design will be the one that most effectively guides visitors from curiosity to belief to participation.
When a visitor reaches the end of the experience, they should feel:
This is bigger than politics.
This is something I can support regardless of party.
This feels credible.
This feels hopeful.
I want to be part of this.
Use the survey results, the research findings, the principles, the storytelling, or any other elements you believe will help build trust and inspire participation.
Don't just impress us with flashy visuals. Impress us with a website experience that inspires people to become part of the movement and cast their vote.
The final call-to-action should feel like the natural conclusion of the journey, not a request for engagement.
Our goal is not simply to inform visitors. Our goal is to inspire them to cast their vote.
Prioritize emotional impact, storytelling, clarity, and persuasion over decorative design elements.
Final words:
Design a website experience that successfully inspires visitors to take the survey and cast their vote.
Think like a storyteller, not just a designer.
Thank you for your interest in the project.
Best of luck.

```html
<!DOCTYPE html>
<html lang="en">
<head>
<meta charset="utf-8">
<title>Lantern Square. Steady Course.</title>
<link href="https://fonts.googleapis.com/css2?family=Libre+Caslon+Text:wght@400;700&family=Inter:wght@400;500;600;700&display=swap" rel="stylesheet">
<style>
:root{
  --stage:#b3b3b3;
  --ink:#0b0a09;
  --card:#181614;
  --line:#2d2a26;
  --cream:#f4ead8;
  --gold:#d0a55e;
  --gold-soft:#e9c88a;
  --band:#dcdce3;
}
*{box-sizing:border-box;margin:0;padding:0}
html,body{width:1200px;height:3592px;overflow:hidden;background:var(--stage)}
body{font-family:"Inter",sans-serif;color:var(--cream)}
.site{position:absolute;left:89px;top:89px;width:1021px;height:3411px;background:var(--ink);overflow:hidden}
section,footer{position:relative;width:1021px}
.serif{font-family:"Libre Caslon Text",serif;font-weight:700;letter-spacing:-0.035em}
.eyebrow{font-size:8px;font-weight:700;letter-spacing:.16em;text-transform:uppercase;color:var(--gold)}
.abs{position:absolute}
.pill{display:inline-flex;align-items:center;justify-content:center;border-radius:999px;font-weight:700;font-size:10px}
.pill-gold{background:linear-gradient(90deg,var(--gold),var(--gold-soft));color:#1a140b}
.pill-dark{background:#12100e;color:var(--cream);border:1px solid #3a342c}

/* hero */
.hero{height:622px}
.hero-photo{position:absolute;inset:0;background:
  radial-gradient(ellipse 45% 40% at 52% 62%,rgba(214,170,100,.55),transparent 70%),
  radial-gradient(ellipse 30% 55% at 15% 40%,rgba(120,95,65,.55),transparent 70%),
  radial-gradient(ellipse 28% 55% at 85% 45%,rgba(110,85,55,.45),transparent 70%),
  linear-gradient(180deg,#1d1812 0%,#3a2c1c 50%,#120e0a 100%)}
.hero-shade{position:absolute;inset:0;background:linear-gradient(180deg,rgba(0,0,0,.25),rgba(0,0,0,0) 40%,rgba(0,0,0,.55))}
.brand{left:18px;top:18px;display:flex;align-items:center;gap:10px}
.brand-mark{width:78px;height:78px;border-radius:50%;border:2px solid var(--gold)}
.brand-name{font-family:"Libre Caslon Text",serif;font-weight:700;font-size:17px;line-height:1.05;color:var(--gold)}
.nav{right:18px;top:21px;display:flex;align-items:center;gap:26px;font-size:11px;font-weight:500}
.nav .vote{border:1px solid var(--cream);border-radius:999px;padding:4px 11px}
.hero-eyebrow{top:105px;width:100%;text-align:center;color:var(--cream);font-size:8px}
.hero-title{top:120px;width:100%;text-align:center;font-size:66px;line-height:72px;color:var(--cream)}
.hero-title .gold{color:var(--gold)}
.hero-sub{top:358px;left:50%;transform:translateX(-50%);width:560px;text-align:center;font-size:18px;line-height:26px;color:#efe6d6}
.hero-cta{top:424px;width:100%;display:flex;justify-content:center;gap:10px}
.hero-cta .pill{height:30px;padding:0 16px}
.stats{top:493px;width:100%;display:flex;justify-content:center;gap:9px}
.stat{width:198px;height:78px;border:1px solid rgba(244,234,216,.22);border-radius:8px;background:rgba(20,16,12,.55);text-align:center;padding-top:10px}
.stat b{display:block;font-family:"Libre Caslon Text",serif;font-size:36px;line-height:42px;font-weight:700;letter-spacing:-0.03em}
.stat span{font-size:7px;letter-spacing:.08em;text-transform:uppercase;color:#d8cdb9}
.scroll{top:590px;width:100%;text-align:center;font-size:7px;letter-spacing:.2em;color:#bdb3a2}

/* mission + story */
.mission{height:1040px;background:linear-gradient(180deg,#0f0e0d,#060606)}
.m-eyebrow{left:237px;top:70px}
.m-title{left:237px;top:84px;width:580px;font-size:42px;line-height:44px}
.m-p{position:absolute;left:237px;font-size:11px;color:#d6cdbf}
.agree{left:237px;top:357px;width:548px;height:66px;border:1px solid var(--line);border-radius:12px;background:#131210;display:flex;align-items:center;justify-content:space-between;padding:0 18px}
.agree .serif{font-size:17px;font-weight:400;letter-spacing:0;color:var(--cream)}
.agree .pill{height:28px;padding:0 15px}
.w-eyebrow{left:163px;top:555px}
.w-title{left:163px;top:568px;font-size:42px;line-height:44px;width:560px}
.w-p{left:163px;top:664px;width:520px;font-size:11px;line-height:19px;color:#d6cdbf}
.timeline{left:163px;top:740px;display:flex;gap:10px}
.step{width:166px;height:185px;border:1px solid var(--line);border-radius:10px;background:#141312;padding:18px 16px}
.step .date{display:inline-block;background:#f1e6d2;color:#1a140b;border-radius:999px;font-size:7px;font-weight:700;padding:3px 8px}
.step h3{font-family:"Libre Caslon Text",serif;font-size:14px;line-height:16px;margin:14px 0 10px;color:var(--cream)}
.step p{font-size:9px;line-height:15px;color:#aba398}
.w-close{top:952px;width:100%;text-align:center;font-family:"Libre Caslon Text",serif;font-size:19px;color:var(--gold-soft)}

/* strip */
.strip{height:201px;background:var(--band)}
.frame{position:absolute;top:26px;height:146px;box-shadow:0 8px 20px rgba(0,0,0,.15)}
.f1{left:0;width:428px;background:linear-gradient(90deg,#9c8a70,#cdbea4 45%,#b9a88c 70%,#e4d8c2)}
.f2{left:447px;width:484px;background:linear-gradient(90deg,#3b3b3b,#8b8b8b 30%,#b77d2f 40%,#8a5a24 55%,#d9d9d9 65%,#555 100%)}
.f3{left:951px;width:70px;background:linear-gradient(90deg,#5a5246,#c7c2b6)}

/* survey */
.survey{height:592px;background:linear-gradient(180deg,#0b0b0a,#120f0b)}
.s-card{left:163px;top:61px;width:695px;height:470px;border:1px solid var(--line);border-radius:14px;background:linear-gradient(180deg,#1c1b1a,#121110);padding:44px 30px 0;display:flex;flex-direction:column;align-items:flex-start}
.s-card .label{font-size:10px;font-weight:700;letter-spacing:.18em;color:#c9bfae;line-height:12px}
.s-card h2{font-size:42px;line-height:44px;margin-top:14px;width:600px}
.s-card p{font-size:10px;line-height:19px;color:#c9c0b3;margin-top:14px;width:630px}
.s-stats{display:flex;gap:9px;margin-top:18px}
.s-stat{width:206px;height:98px;border:1px solid var(--line);border-radius:10px;background:#0d0c0b;padding:12px 16px}
.s-stat b{display:block;font-family:"Libre Caslon Text",serif;font-size:46px;line-height:56px;color:var(--gold-soft);letter-spacing:-0.03em}
.s-stat span{font-size:7px;letter-spacing:.08em;color:#8f877b}
.bars{margin-top:18px;width:100%}
.bar{display:flex;align-items:center;height:19.5px;font-size:8px;color:#d8cfc1}
.bar .name{width:77px}
.bar .track{width:520px;height:6px}
.bar .fill{display:block;height:6px;border-radius:3px;background:linear-gradient(90deg,var(--gold),var(--gold-soft))}
.bar .val{margin-left:auto}
.s-card .pill{margin-top:14px;height:24px;padding:0 12px;font-size:7px;letter-spacing:.1em;background:#141210;color:var(--cream);border:1px solid #3a342c}

/* principles */
.principles{height:341px;background:#0a0908;text-align:center}
.p-eyebrow{top:68px;width:100%}
.p-title{top:82px;width:100%;font-size:42px;line-height:44px}
.p-sub{top:188px;width:100%;font-size:11px;color:#c9c0b3}
.p-btn{top:220px;width:100%;display:flex;justify-content:center}
.p-btn .pill{height:25px;padding:0 14px;font-size:7px;letter-spacing:.1em;background:#141210;color:var(--cream);border:1px solid #3a342c}

/* cta */
.cta{height:551px;text-align:center;background:radial-gradient(ellipse 55% 45% at 50% 55%,#3a2e1e,#0c0a08 75%),#0c0a08}
.cta-flag{left:496px;top:48px;width:166px;height:78px;opacity:.25;background:linear-gradient(180deg,#6a5a48,#2a241d)}
.c-eyebrow{top:135px;width:100%;font-size:11px;color:#d8cdb9;letter-spacing:.22em}
.c-title{top:157px;width:100%;font-size:42px;line-height:44px}
.c-p{top:258px;left:50%;transform:translateX(-50%);width:540px;font-size:11px;line-height:20px;color:#d2c9bb}
.c-btn{top:334px;width:100%;display:flex;justify-content:center}
.c-btn .pill{height:32px;padding:0 20px;font-size:11px}
.c-count{top:385px;width:100%;font-family:"Libre Caslon Text",serif;font-size:32px;color:var(--gold-soft)}
.c-label{top:426px;width:100%;font-size:7px;letter-spacing:.1em;color:#c9bfae}

footer{height:64px;background:#0d0c0b;font-size:8px;color:#9a9185}
.f-copy{left:163px;top:34px}
.f-top{left:813px;top:25px}
</style>
</head>
<body>
<main class="site">

  <section class="hero">
    <div class="hero-photo" role="img" aria-label="Cinematic sepia scene: historic statesman in profile, domed capitol at dusk, young woman looking toward the horizon"></div>
    <div class="hero-shade"></div>
    <div class="abs brand">
      <span class="brand-mark"></span>
      <span class="brand-name">Lantern Square,<br>Steady Course.</span>
    </div>
    <nav class="abs nav">
      <span>HOME</span><span>MISSION</span><span>PRINCIPLES</span><span>RESULTS</span><span class="vote">VOTE NOW</span>
    </nav>
    <p class="abs eyebrow hero-eyebrow">A Bipartisan Civic Movement</p>
    <h1 class="abs serif hero-title">Lantern<br>Square.<br><span class="gold">Steady Course.</span></h1>
    <p class="abs hero-sub">Americans deserve a government that is legally required to serve them honestly.</p>
    <div class="abs hero-cta"><span class="pill pill-gold">Cast Your Vote</span><span class="pill pill-dark">Watch the Story</span></div>
    <div class="abs stats">
      <div class="stat"><b>82.9</b><span>% said yes in a ballot vote</span></div>
      <div class="stat"><b>89.9</b><span>% agree with the 7 principles</span></div>
      <div class="stat"><b>1,016</b><span>people already voted yes</span></div>
    </div>
    <p class="abs scroll">SCROLL</p>
  </section>

  <section class="mission">
    <p class="abs eyebrow m-eyebrow">Mission Statement</p>
    <h2 class="abs serif m-title">Today, not a single law binds our government to act honestly, and in our best interest.</h2>
    <p class="m-p" style="top:292px">If our government exists solely to serve us, why isn't it legally required to?</p>
    <p class="m-p" style="top:323px">We founded this movement to change that.</p>
    <div class="abs agree"><span class="serif">Do you agree?</span><span class="pill pill-gold">Vote Now</span></div>

    <p class="abs eyebrow w-eyebrow">Who We Are</p>
    <h2 class="abs serif w-title">From a simple idea to a national framework.</h2>
    <p class="abs w-p">A bipartisan movement based in Washington, D.C., built around one simple idea: government should faithfully serve the people, not special interests.</p>
    <div class="abs timeline">
      <article class="step"><span class="date">August 2024</span><h3>The nonprofit began</h3><p>We started a nonprofit with one goal in mind: Americans deserve an honest government.</p></article>
      <article class="step"><span class="date">October 2025</span><h3>The principles emerged</h3><p>We identified 10 principles that most Americans agree our government must uphold.</p></article>
      <article class="step"><span class="date">March 2026</span><h3>The framework formed</h3><p>We turned those principles into a rigorous framework and named it Lantern Square, Steady Course.</p></article>
      <article class="step"><span class="date">April 2026</span><h3>The study was tested</h3><p>We tested the framework in a pre-registered national study with Americans across the political spectrum.</p></article>
    </div>
    <p class="abs w-close">And the results exceeded all our expectations.</p>
  </section>

  <section class="strip">
    <div class="frame f1" role="img" aria-label="Archival sepia photographs of early suffrage marchers with a flag"></div>
    <div class="frame f2" role="img" aria-label="Archival photographs of civil rights era leaders"></div>
    <div class="frame f3" role="img" aria-label="Archival photograph of soldiers near a capitol dome"></div>
  </section>

  <section class="survey">
    <div class="abs s-card">
      <p class="label">THE SURVEY</p>
      <h2 class="serif">Support held across party lines.</h2>
      <p>We laid out the principles, then asked Americans if they would support a legal framework built around them. Most reforms lose support once the details appear. This one didn't.</p>
      <div class="s-stats">
        <div class="s-stat"><b>82.9</b><span>% SAID YES</span></div>
        <div class="s-stat"><b>89.9</b><span>% AGREE</span></div>
        <div class="s-stat"><b>2.7</b><span>% OPPOSED</span></div>
      </div>
      <div class="bars">
        <div class="bar"><span class="name">Democrats</span><span class="track"><span class="fill" style="width:84.5%"></span></span><span class="val">84.5%</span></div>
        <div class="bar"><span class="name">Republicans</span><span class="track"><span class="fill" style="width:80.2%"></span></span><span class="val">80.2%</span></div>
        <div class="bar"><span class="name">Independents</span><span class="track"><span class="fill" style="width:79.9%"></span></span><span class="val">79.9%</span></div>
      </div>
      <span class="pill">READ THE DETAILS OF THE STUDY</span>
    </div>
  </section>

  <section class="principles">
    <p class="abs eyebrow p-eyebrow">The Seven Principles</p>
    <h2 class="abs serif p-title">What honest public<br>service should require.</h2>
    <p class="abs p-sub">89.9% of Americans said they agree.</p>
    <div class="abs p-btn"><span class="pill">READ THE PRINCIPLES</span></div>
  </section>

  <section class="cta">
    <div class="abs cta-flag" role="img" aria-label="Faint photograph of a waving flag"></div>
    <p class="abs c-eyebrow">ONE MINUTE. ONE VOICE.</p>
    <h2 class="abs serif c-title">Be part of history. Vote<br>now.</h2>
    <p class="abs c-p">For decades, we have argued over policies, parties, and ideologies. But today, across political lines, generations, and races, Americans are arriving at the same conclusion: we deserve a government legally required to serve the people honestly.</p>
    <div class="abs c-btn"><span class="pill pill-gold">Take the 1-Minute Survey</span></div>
    <p class="abs c-count">1,016</p>
    <p class="abs c-label">PEOPLE ALREADY VOTED YES FOR THE BALLOT</p>
  </section>

  <footer>
    <p class="abs f-copy">© 2026 Lantern Square. Steady Course.</p>
    <p class="abs f-top">Back to top</p>
  </footer>

</main>
</body>
</html>
```